Brixelo Photography Business Cards

We need a good general business card that we can hand to our clients. We will be doing embossed gloss cards.

Target Market(s)

Real estate / Business to business / professionals

```html
<!DOCTYPE html>
<html lang="en">
<head>
<meta charset="utf-8">
<title>Brixelo Photography Business Cards</title>
<link rel="stylesheet" href="https://fonts.googleapis.com/css2?family=Open+Sans:ital,wght@0,400;0,700;0,800;1,400&display=swap">
<style>
  :root {
    --backdrop: #c9c9c9;
    --navy: #28235f;
    --navy-soft: #332d72;
    --navy-edge: #3c3680;
    --sky: #2aa3dc;
    --ink: #1f1f2b;
    --paper: #ffffff;
    --ghost: #ececec;
  }
  * { margin: 0; padding: 0; box-sizing: border-box; }
  html, body {
    width: 1200px; height: 900px; overflow: hidden;
    background: var(--backdrop);
    font-family: "Open Sans", Arial, sans-serif;
  }
  .sheet { position: relative; width: 1200px; height: 900px; }

  .card {
    position: absolute;
    width: 630px; height: 360px;
    left: 285px;
    overflow: hidden;
    box-shadow: 0 6px 14px rgba(0,0,0,0.25);
  }

  /* Back of card */
  .card-back { top: 60px; background: var(--navy); }
  .card-back .seal {
    position: absolute; left: 50%; top: 50%;
    width: 220px; height: 220px;
    margin: -110px 0 0 -110px;
    border: 3px solid var(--navy-edge);
    border-radius: 50%;
  }
  .card-back .seal-name {
    position: absolute; left: 0; right: 0; top: 50%;
    transform: translateY(-50%);
    text-align: center;
    font-weight: 700; font-size: 22px;
    color: var(--navy-edge);
    letter-spacing: 0.5px;
  }

  /* Front of card */
  .card-front { top: 480px; background: var(--paper); }
  .card-front .watermark-ring {
    position: absolute; left: -70px; top: 10px;
    width: 340px; height: 340px;
    border: 10px solid var(--ghost);
    border-radius: 50%;
  }
  .card-front .watermark-name {
    position: absolute; left: -40px; top: 262px;
    font-weight: 700; font-size: 40px;
    color: var(--ghost);
    white-space: nowrap;
  }
  .holder {
    position: absolute; left: 44px; top: 140px;
  }
  .holder-name {
    font-weight: 800; font-size: 20px;
    color: var(--navy); letter-spacing: 0.3px;
  }
  .holder-role {
    font-style: italic; font-size: 14px; color: var(--ink);
  }
  .brand-name {
    position: absolute; right: 40px; top: 58px;
    font-weight: 700; font-size: 30px;
    color: var(--navy); white-space: nowrap;
  }
  .contact {
    position: absolute; left: 352px; top: 216px;
    font-size: 15px; color: var(--ink); line-height: 1.3;
  }
  .address { margin-bottom: 6px; }
  .contact-line { display: flex; align-items: center; gap: 7px; }
  .contact-line svg { width: 15px; height: 15px; flex: none; }
</style>
</head>
<body>
<main class="sheet">

  <section class="card card-back" aria-label="Card back">
    <div class="seal"></div>
    <div class="seal-name">Brixelo Photography</div>
  </section>

  <section class="card card-front" aria-label="Card front">
    <div class="watermark-ring"></div>
    <div class="watermark-name">Brixelo Photography</div>

    <div class="holder">
      <p class="holder-name">DANIEL HARROW</p>
      <p class="holder-role">Owner</p>
    </div>

    <p class="brand-name">Brixelo Photography</p>

    <div class="contact">
      <p class="address">418 N. W. 5th Street<br>Tampa, Florida, 33602</p>
      <p class="contact-line">
        <svg viewBox="0 0 16 16" aria-hidden="true"><path fill="#2aa3dc" d="M3.6 1.2l2.2 2.6-1.3 1.7c.9 2 2.3 3.4 4.3 4.4l1.7-1.3 2.6 2.2-1.4 2.4C7 12.7 3.3 9 1.2 3z"/></svg>
        (555) 214-3097
      </p>
      <p class="contact-line">
        <svg viewBox="0 0 16 16" aria-hidden="true"><rect x="1" y="3" width="14" height="10" fill="none" stroke="#2aa3dc" stroke-width="1.4"/><path d="M1 3l7 6 7-6" fill="none" stroke="#2aa3dc" stroke-width="1.4"/></svg>
        daniel@brixelophoto.com
      </p>
      <p class="contact-line">
        <svg viewBox="0 0 16 16" aria-hidden="true"><g fill="none" stroke="#2aa3dc" stroke-width="1.2"><circle cx="8" cy="8" r="6.5"/><ellipse cx="8" cy="8" rx="3" ry="6.5"/><path d="M1.5 8h13M2.5 4.8h11M2.5 11.2h11"/></g></svg>
        www.brixelophoto.com
      </p>
    </div>
  </section>

</main>
</body>
</html>
```